Harbor Gate Advisory

KRT W.K.R.B./ENVIRONMENTAL MANAGEMENT. Member of N.P.C.T., G.L.U.K.. T.O.R.V., H.M.E.P. W.K.R.B. 10/20/30 hr. GENERAL INDUSTRY CERTIFIED, HAZMAT CERTIFIED, CONSTRUCTION SAFETY CERTIFIED, W.K.R.B. LOG, LOSS PREVENTION SOLUTIONS, WILL WRITE SAFETY PROTOCOL PROGRAMS ACCORDING TO LOCAL AND STATE CODES/STANDARDS. INSPECT YOUR PLACE OF BUSINESS INSIDE AND OUT SIDE INFRASTRUCTURE INCLUDING SAFETY INSPECTION PROTOCOL REGARDING EQUIPMENT, PUMP HOUSE, COMPRESSOR LOG AND FIRE RISERS MANDATES. CONDUCT FIRE EVACUATIONS AND CREATE EVACUATION MASS AS REQUIRED BY LAW. TRAINING YOU AND YOUR SUPERVISORS TO CREATE A SAFETY CULTURE. INVESTIGATE ACCIDENTS AND DOCUMENT FOLLOW UP. WALK WITH CITY AND STATE CODES COMPLIANCE OFFICERS AS A CONDUCT AND AND FOLLOW THROUGH WITH REQUIRED CHANCES IN CODE COMPLIANCE. 15 YEARS EXPERIENCE.

Target Market(s)

businesses with 11+ employees as mandated by Federal law. Business owners.

Industry/Entity Type

Business

Contact Information for Business Card

MARCIA L. FONTAINE
913 N.E. WILLOWBANK LANE
PORT SAINT LUCIE , FLORIDA
27618-4402

www.harborgateadvisory.us
Rkt481@quellmail.net
(877) 615-3042

Requirements
Must have
• Safety training, inspections, images, knowledge, teamwork, safety culture, safe workplace, compliance, 15 years experience, training documenting all trying development, trying needs analysis, proactive and reactive observations, technical writing programs, creating power point materials for training modules, excel spreadsheet.

```html
<!DOCTYPE html>
<html lang="en">
<head>
<meta charset="utf-8">
<title>Harbor Gate Advisory – Business Card</title>
<link rel="stylesheet" href="https://fonts.googleapis.com/css2?family=Marcellus&family=Open+Sans:wght@400;600;700&display=swap">
<style>
  :root {
    --stage-top: #d4d4d4;
    --stage-bottom: #fafafa;
    --navy: #1c1c3e;
    --navy-deep: #101028;
    --navy-mid: #2a2a56;
    --silver-light: #f2f2f2;
    --silver-mid: #b9b9c2;
    --silver-dark: #7c7c88;
    --ink-white: #ffffff;
    --photo-light: #e8e9ee;
    --photo-dark: #aeb2c2;
  }
  * { box-sizing: border-box; margin: 0; padding: 0; }
  html, body { width: 1200px; height: 900px; overflow: hidden; }
  body {
    background: linear-gradient(180deg, var(--stage-top) 0%, var(--stage-bottom) 60%, #ffffff 100%);
    font-family: "Open Sans", Arial, sans-serif;
    position: relative;
  }
  .card {
    position: absolute;
    top: 300px;
    width: 530px;
    height: 303px;
    border-radius: 22px;
    overflow: hidden;
    box-shadow: 0 14px 28px rgba(0,0,0,0.25);
  }
  /* Front */
  .card-front { left: 45px; background: var(--ink-white); }
  .front-top { position: absolute; left: 0; top: 0; width: 100%; height: 160px; background: var(--ink-white); }
  .photo {
    position: absolute;
    bottom: 0;
    width: 110px;
    height: 150px;
    background: linear-gradient(180deg, var(--photo-light) 0%, var(--photo-dark) 100%);
    opacity: 0.75;
    border-radius: 8px 8px 0 0;
  }
  .photo-left { left: 8px; }
  .photo-right { right: 12px; }
  .brand {
    position: absolute;
    left: 50%;
    top: 24px;
    transform: translateX(-50%);
    text-align: center;
    width: 280px;
  }
  .brand-mark {
    display: block;
    width: 78px;
    height: 78px;
    border-radius: 50%;
    background: var(--navy-mid);
    margin: 0 auto 14px;
  }
  .brand-name {
    font-family: "Marcellus", Georgia, serif;
    font-size: 20px;
    color: var(--navy);
    letter-spacing: 0.3px;
    white-space: nowrap;
  }
  .silver-band {
    position: absolute;
    left: 0; top: 160px;
    width: 100%; height: 12px;
    background: linear-gradient(90deg, var(--silver-dark), var(--silver-light) 45%, var(--silver-mid) 100%);
  }
  .front-bottom {
    position: absolute;
    left: 0; top: 172px;
    width: 100%; height: 131px;
    background: linear-gradient(180deg, var(--navy-mid) 0%, var(--navy) 50%, var(--navy-deep) 100%);
    text-align: center;
    color: var(--ink-white);
  }
  .holder-name {
    margin-top: 8px;
    font-size: 21px;
    font-weight: 700;
    letter-spacing: 1.5px;
    color: var(--silver-mid);
  }
  .contact-line { font-size: 12px; line-height: 17px; }
  .contact-line.address { font-size: 11px; margin-top: 4px; }
  .contact-line.phone { font-size: 14px; font-weight: 600; }
  /* Back */
  .card-back {
    left: 625px;
    background: linear-gradient(180deg, var(--navy-mid) 0%, var(--navy) 45%, var(--navy-deep) 100%);
    display: flex;
    align-items: center;
    justify-content: center;
  }
  .services {
    list-style: none;
    text-align: center;
    color: var(--ink-white);
    font-size: 11.5px;
    letter-spacing: 1.4px;
    line-height: 17px;
  }
</style>
</head>
<body>
  <section class="card card-front">
    <div class="front-top">
      <div class="photo photo-left" role="img" aria-label="Photo of a uniformed security officer"></div>
      <div class="photo photo-right" role="img" aria-label="Photo of a uniformed security officer speaking into a radio"></div>
      <div class="brand">
        <span class="brand-mark"></span>
        <div class="brand-name">HARBOR GATE ADVISORY</div>
      </div>
    </div>
    <div class="silver-band"></div>
    <div class="front-bottom">
      <div class="holder-name">MARCIA L. FONTAINE</div>
      <div class="contact-line address">913 N.E. WILLOWBANK LANE PORT SAINT LUCIE , FLORIDA</div>
      <div class="contact-line phone">877-615-3042</div>
      <div class="contact-line">www.harborgateadvisory.us</div>
      <div class="contact-line">Rkt481@quellmail.net</div>
    </div>
  </section>

  <section class="card card-back">
    <ul class="services">
      <li>SAFETY TRAINING</li>
      <li>INSPECTIONS</li>
      <li>IMAGES</li>
      <li>KNOWLEDGE</li>
      <li>TEAMWORK</li>
      <li>SAFETY CULTURE</li>
      <li>SAFE WORKPLACE</li>
      <li>COMPLIANCE</li>
      <li>15 YEARS EXPERIENCE</li>
      <li>TRAINING DOCUMENTING ALL TRAINING DEVELOPMENT</li>
      <li>TRAINING NEEDS ANALYSIS</li>
      <li>PROACTIVE AND REACTIVE OBSERVATIONS</li>
      <li>TECHNICAL WRITING PROGRAMS</li>
      <li>CREATING POWER POINT MATERIALS FOR TRAINING MODULES</li>
      <li>EXCEL SPREADSHEET</li>
    </ul>
  </section>
</body>
</html>
```